Bright Path Floor Finishes - Builders Flyer

The goal of this flyer is to sell our services to home builders to include our services as an upgrade for new home purchases.
Flyer should be two sided full color.
Colors, font, look/feel should match company website.
Our company is "Bright Path Floor Finishes".
We specialize in decorative concrete coatings; including Concrete staining and sealing, Epoxy flake and quartz, Polished Concrete, Concrete resurfacing & overlay, Concrete crack repairs, Pool deck spray texture and Stamped concrete.
Applications include: Garages, Patios, Pool decks, Driveways, Basements, Counter & Bar tops.
See attached files for company logo, contact info and project photos.

```html
<!DOCTYPE html>
<html lang="en">
<head>
<meta charset="utf-8">
<title>Bright Path Floor Finishes – Builders Flyer</title>
<link rel="stylesheet" href="https://fonts.googleapis.com/css2?family=Montserrat:wght@300;400;500;600;700;800&family=Bebas+Neue&family=Dancing+Script:wght@500&display=swap">
<style>
  :root{
    --brown:#733a2b;
    --brown-dark:#5c2e22;
    --tan:#e9b97f;
    --tan-text:#e0a96a;
    --grey:#c9c9cc;
    --page-left:#f8f9fb;
    --page-right:#ffffff;
    --ink:#2b2b2b;
  }
  *{margin:0;padding:0;box-sizing:border-box}
  html,body{width:1200px;height:794px;overflow:hidden;background:#fff}
  body{font-family:"Montserrat",sans-serif;color:var(--ink)}
  .flyer{position:relative;width:1200px;height:794px;background:var(--page-right);overflow:hidden}
  .page-left{position:absolute;left:0;top:0;width:600px;height:794px;background:var(--page-left)}
  .abs{position:absolute}

  /* brand */
  .brand{left:41px;top:80px;display:flex;align-items:center;gap:10px}
  .brand-square{width:30px;height:30px;background:var(--brown)}
  .brand-name{font-weight:800;font-size:21px;color:#1e1e1e;letter-spacing:.2px;line-height:1}

  .headline{left:41px;top:154px;font-family:"Bebas Neue",sans-serif;font-size:38px;color:var(--brown);letter-spacing:.5px;line-height:1}
  .cert-band{left:0;top:193px}
  .cert-text{left:41px;top:195px;width:465px;white-space:nowrap;font-family:"Bebas Neue",sans-serif;font-size:22px;color:#fff;letter-spacing:0;line-height:28px}

  .specialize{left:41px;top:256px;font-weight:800;font-size:23px;color:var(--brown);line-height:1}
  .script{left:41px;top:280px;font-family:"Dancing Script",cursive;font-size:23px;color:var(--tan-text);line-height:1.2}
  .intro{left:41px;top:320px;width:236px;font-weight:300;font-size:17.5px;line-height:21.2px;color:var(--tan-text)}
  .list-title{font-weight:600;font-size:14px;color:var(--tan-text);line-height:1.2}
  .list{font-weight:300;font-size:13px;line-height:16.5px;color:var(--tan-text)}
  .applications{left:37px;top:528px;width:240px}
  .benefits{left:37px;top:642px;width:230px}

  .divider-v{left:299px;top:264px;width:1px;height:462px;background:var(--tan)}

  .services-title{left:318px;top:265px;font-weight:700;font-size:15px;color:var(--brown);line-height:1}
  .service{position:absolute;width:120px}
  .service-label{font-weight:700;font-size:8px;color:var(--tan-text);line-height:10px;height:22px;text-transform:uppercase}
  .service-photo{width:91px;height:93px;border:3px solid var(--tan);border-radius:12px}
  .s-epoxy .service-photo{background:linear-gradient(160deg,#6e5a48,#4b2f1c 55%,#8a4f24)}
  .s-stamped .service-photo{background:linear-gradient(180deg,#dfe8ef 0%,#7fa25a 35%,#6d5a4b 60%,#4c3a2f)}
  .s-staining .service-photo{background:radial-gradient(circle at 40% 30%,#c47a3e,#6b3413 70%)}
  .s-polished .service-photo{background:radial-gradient(circle at 50% 40%,#b9ab9c,#6f5d4d 80%)}
  .s-overlay .service-photo{background:linear-gradient(135deg,#8f9294,#585d60 60%,#9fb2b8)}
  .s-counter .service-photo{background:linear-gradient(180deg,#5a3a2a,#8b3b2c 45%,#2a1e1a)}

  /* right page */
  .why-panel{left:600px;top:54px}
  .why-title{left:656px;top:58px;font-weight:700;font-size:21px;color:var(--brown-dark);line-height:1}
  .why-list{left:656px;top:85px;width:360px;font-size:17px;line-height:21.5px;color:#fff;font-weight:400;list-style:none}

  .reviews-tab{left:600px;top:270px}
  .reviews-title{left:650px;top:274px;font-weight:700;font-size:18px;color:var(--brown-dark);line-height:1}
  .divider-rv{left:890px;top:274px;width:1px;height:327px;background:var(--tan)}
  .divider-rh{left:647px;top:419px;width:486px;height:1px;background:#d8d0c8}

  .rating{font-size:14px;line-height:16.5px;color:#222;font-weight:400}
  .badge{width:66px;height:91px;border-radius:8px;background:linear-gradient(160deg,#9aa3ad,#4e5966)}
  .badge-round{display:flex;align-items:center;justify-content:center}
  .badge-round span{width:56px;height:56px;border-radius:50%;background:#2f3f8f;border:3px solid #d9dbe0}

  .review-col{width:226px}
  .review-head{font-size:14px;line-height:16.5px;color:#222;margin-bottom:8px}
  .review-text{font-size:7.6px;line-height:9.4px;color:#222;margin-bottom:8px}

  .cta{left:660px;top:637px;width:484px;text-align:center;color:var(--brown-dark)}
  .cta-1{font-weight:700;font-size:16px;line-height:20px}
  .cta-2{font-weight:700;font-size:16px;line-height:20px}
  .cta-3{font-weight:400;font-size:13.5px;line-height:22px;color:#222}

  .contact-band{left:600px;top:705px}
  .owner{left:640px;top:714px;text-align:right;width:180px;color:var(--brown-dark)}
  .owner-name{font-weight:700;font-size:18px;line-height:20px}
  .owner-role{font-weight:500;font-size:11.5px;line-height:14px}
  .phone{left:862px;top:713px;font-weight:700;font-size:31px;line-height:40px;color:var(--brown-dark);letter-spacing:.3px;white-space:nowrap}
</style>
</head>
<body>
<div class="flyer">

  <section class="page-left">
    <div class="abs brand"><span class="brand-square"></span><span class="brand-name">Bright Path Floor Finishes</span></div>

    <h1 class="abs headline">Bright Path Floors</h1>
    <svg class="abs cert-band" width="600" height="28" viewBox="0 0 600 28" aria-hidden="true">
      <polygon points="0,0 521,0 510,28 0,28" fill="var(--tan)"/>
      <polygon points="530,0 545,0 534,28 519,28" fill="var(--grey)"/>
      <polygon points="555,0 570,0 559,28 544,28" fill="var(--brown)"/>
      <polygon points="580,0 595,0 584,28 569,28" fill="var(--tan)"/>
    </svg>
    <p class="abs cert-text">Is a proud certified installer of Summit Crete products</p>

    <h2 class="abs specialize">WE SPECIALIZE IN</h2>
    <p class="abs script">decorative concrete coatings</p>
    <p class="abs intro">Including concrete staining and sealing, epoxy flake and quartz, polished concrete, concrete resurfacing &amp; overlay, concrete crack repairs, pool deck spray texture and stamped concrete.</p>

    <div class="abs applications">
      <h3 class="list-title">&nbsp;Applications</h3>
      <p class="list">· Garages · Patios · Pool decks<br>· Driveways · Basements<br>· Counter &amp; Bar tops</p>
    </div>

    <div class="abs benefits">
      <h3 class="list-title">Benefits</h3>
      <p class="list">&nbsp;· Offer customers specialty upgrades<br>&nbsp;· Provide market differentiator<br>&nbsp;· Increase home market valu</p>
    </div>

    <div class="abs divider-v"></div>

    <h2 class="abs services-title">OUR SERVICES</h2>
    <div class="service s-epoxy" style="left:321px;top:290px">
      <p class="service-label">Decorative epoxy<br>coating</p>
      <div class="service-photo" role="img" aria-label="Photo of a decorative epoxy coated floor"></div>
    </div>
    <div class="service s-stamped" style="left:456px;top:290px">
      <p class="service-label">Concrete stamped</p>
      <div class="service-photo" role="img" aria-label="Photo of a stamped concrete patio with stone fireplace"></div>
    </div>
    <div class="service s-staining" style="left:321px;top:456px">
      <p class="service-label">Concrete staining</p>
      <div class="service-photo" role="img" aria-label="Photo of a stained concrete floor"></div>
    </div>
    <div class="service s-polished" style="left:456px;top:456px">
      <p class="service-label">Polished concrete</p>
      <div class="service-photo" role="img" aria-label="Photo of a polished concrete floor"></div>
    </div>
    <div class="service s-overlay" style="left:321px;top:605px">
      <p class="service-label">Overlay &amp;<br>resurfacing</p>
      <div class="service-photo" role="img" aria-label="Photo of a resurfaced concrete pool deck"></div>
    </div>
    <div class="service s-counter" style="left:456px;top:605px">
      <p class="service-label">Countertops &amp; custom<br>projects</p>
      <div class="service-photo" role="img" aria-label="Photo of a custom concrete bar top with stools"></div>
    </div>
  </section>

  <section class="page-right">
    <svg class="abs why-panel" width="552" height="193" viewBox="0 0 552 193" aria-hidden="true">
      <polygon points="0,0 552,0 433,193 0,193" fill="var(--brown)"/>
      <polygon points="0,0 177,0 157,28 0,28" fill="var(--tan)"/>
    </svg>
    <h2 class="abs why-title">Why Us?</h2>
    <ul class="abs why-list">
      <li>&nbsp;· Proven residential and commercial track record</li>
      <li>&nbsp;· Reliable &amp; quality workmanship</li>
      <li>&nbsp;· Best in industry products</li>
      <li>&nbsp;· Family owned and operated</li>
      <li>&nbsp;· Exclusive service provider for Harbor &amp; Whitfield Homes</li>
    </ul>

    <svg class="abs reviews-tab" width="246" height="28" viewBox="0 0 246 28" aria-hidden="true">
      <polygon points="0,0 246,0 226,28 0,28" fill="var(--tan)"/>
    </svg>
    <h2 class="abs reviews-title">Reviews &amp; Ratings</h2>
    <div class="abs divider-rv"></div>
    <div class="abs divider-rh"></div>

    <p class="abs rating" style="left:650px;top:311px">Trusted Trade<br>Council A+ Rating</p>
    <div class="abs badge" style="left:786px;top:311px" aria-hidden="true"></div>

    <p class="abs rating" style="left:939px;top:311px">Voted Best<br>of Elm County<br>2019-2024</p>
    <div class="abs badge badge-round" style="left:1040px;top:311px" aria-hidden="true"><span></span></div>

    <div class="abs review-col" style="left:650px;top:427px">
      <p class="review-head">FriendSpot Reviews<br>5 Star Rating</p>
      <p class="review-text">"Sam was highly professional; he offered a competitive price, showed up when he told us he would, completed the job by the requested date, was flexible in working around my crazy work schedule, and was always clear in his communications. I would hire him again in a heartbeat and I recommend him highly." ~ Mark Dalton</p>
      <p class="review-text">· "Does amazing work. Is very reliable and has great prices! Highly recommended." ~ Lena Morris<br>FriendSpot Page</p>
    </div>
    <div class="abs review-col" style="left:937px;top:427px">
      <p class="review-head">SearchStar Reviews<br>5 Star Rating</p>
      <p class="review-text">· "Sam's attention to detail is superb, he treats his jobs like he was doing his house! Highly recommend Sam at Bright Path Floors, he is awesome, and his prices are very fair especially for the quality he delivers!" ~ Paul Hardin</p>
      <p class="review-text">· Not only do they do amazing work, but the owner was on site every day, extremely responsive, timely, and professional. It's hard to find workmanship like that these days. ~ Rita Fowler</p>
    </div>

    <div class="abs cta">
      <p class="cta-1">DON'T KNOW WHAT YOU'RE LOOKING FOR YET?</p>
      <p class="cta-2">Find the best fit for your application</p>
      <p class="cta-3">Tell us about your project!</p>
    </div>

    <svg class="abs contact-band" width="548" height="60" viewBox="0 0 548 60" aria-hidden="true">
      <polygon points="0,0 548,0 512,60 0,60" fill="var(--tan)"/>
    </svg>
    <div class="abs owner">
      <p class="owner-name">SAM ORTEGA</p>
      <p class="owner-role">Owner/Operator</p>
    </div>
    <p class="abs phone">404-555-0142</p>
  </section>

</div>
</body>
</html>
```